I need a new business card design for my pharmacy.

I need a business card design. I will include my logo.
The card needs to be readable. I prefer to have my logo on one side along with my website, the other side includes the other information. Please use combination of black, neon green, white, and silver. This needs to catch the eye but yet be clearly visible and legible. Thanks

Industry/Entity Type

Pharmacy

Contact Information for Business Card

It needs to have the following information listed:
Mel's Apothecary Owner/Pharm D.
7134 North Brook Lane
Maple Ridge, ND 58214
Phone 555-318-6207
Fax 555-318-6209
email: mel@melsapothecary-example.com
www.melsapothecary-example.com
Store hours Monday-Friday 9 am- 6 pm
Saturday 9 am- 1 pm
Sunday Closed
Please utilize the colors black, white, and neon green, maybe silver.

Requirements
Must have
• It needs to be easily readable!
Nice to have
• It should catch the eye.
Should not have
• Do not use any other colors except listed: black, neon green, white, & silver.

```html
<!DOCTYPE html>
<html lang="en">
<head>
<meta charset="utf-8">
<title>Mel's Apothecary – Business Card</title>
<link rel="stylesheet" href="https://fonts.googleapis.com/css2?family=Open+Sans:wght@400;600;700;800&display=swap">
<style>
  :root {
    --neon: #a6ce39;
    --ink: #1a1a1a;
    --paper: #ffffff;
    --backdrop: #e9e9e9;
  }
  * { box-sizing: border-box; margin: 0; padding: 0; }
  html, body {
    width: 1200px; height: 900px; overflow: hidden;
    background: var(--backdrop);
    font-family: "Open Sans", Arial, sans-serif;
    color: var(--ink);
  }
  .stage {
    position: relative; width: 1200px; height: 900px;
    display: flex; flex-direction: column; align-items: center; justify-content: center; gap: 50px;
  }
  .card {
    position: relative; width: 700px; height: 400px;
    background: var(--paper); overflow: hidden;
    box-shadow: 0 6px 18px rgba(0,0,0,.18);
  }

  /* Front: contact side */
  .front .owner { position: absolute; left: 44px; top: 40px; }
  .front .owner-name { font-size: 27px; font-weight: 800; letter-spacing: .2px; line-height: 1.1; }
  .front .owner-name .accent { color: var(--neon); }
  .front .owner-title { font-size: 18px; font-weight: 600; margin-top: 4px; }
  .front .owner-title .accent { color: var(--neon); }
  .contact-list { position: absolute; left: 44px; top: 132px; list-style: none; }
  .contact-list li {
    display: flex; align-items: flex-start; gap: 14px;
    font-size: 14px; line-height: 1.35; margin-bottom: 9px; font-weight: 600;
  }
  .contact-list svg { width: 18px; height: 18px; flex: none; fill: var(--neon); }
  .brand-lockup {
    position: absolute; right: 52px; top: 118px;
    display: flex; align-items: center; gap: 14px;
  }
  .brand-lockup .dot { width: 30px; height: 30px; border-radius: 50%; background: var(--neon); }
  .brand-lockup .brand-name { font-size: 28px; font-weight: 600; letter-spacing: -.3px; }
  .store-hours {
    position: absolute; left: 44px; bottom: 62px;
    font-size: 11.5px; font-weight: 700; font-variant: small-caps; letter-spacing: .2px;
  }
  .store-hours .label, .store-hours .time { color: var(--neon); }
  .front .base-band {
    position: absolute; left: 0; right: 0; bottom: 0; height: 30px;
    background: var(--neon); border-top: 4px solid var(--ink);
  }

  /* Back: brand side */
  .back .band { position: absolute; left: 0; right: 0; background: var(--neon); }
  .back .band-top { top: 26px; height: 88px; border-bottom: 4px solid var(--ink); }
  .back .band-bottom { bottom: 26px; height: 96px; border-top: 4px solid var(--ink); }
  .back .brand-block {
    position: absolute; left: 0; right: 0; top: 118px; height: 152px;
    display: flex; flex-direction: column; align-items: center; justify-content: center;
  }
  .back .brand-lockup { position: static; gap: 18px; }
  .back .brand-lockup .dot { width: 36px; height: 36px; }
  .back .brand-lockup .brand-name { font-size: 38px; }
  .back .website { color: var(--neon); font-size: 19px; font-weight: 600; margin-top: 6px; margin-left: 140px; }
</style>
</head>
<body>
<main class="stage">

  <section class="card front" aria-label="Card front, contact details">
    <div class="owner">
      <h1 class="owner-name">MEL'S <span class="accent">APOTHECARY</span></h1>
      <p class="owner-title"><span class="accent">PHARM</span> D.</p>
    </div>

    <ul class="contact-list">
      <li>
        <svg viewBox="0 0 24 24" aria-hidden="true"><path d="M6.6 10.8a15.1 15.1 0 0 0 6.6 6.6l2.2-2.2c.3-.3.7-.4 1-.2 1.1.4 2.3.6 3.6.6.6 0 1 .4 1 1V20c0 .6-.4 1-1 1A17 17 0 0 1 3 4c0-.6.4-1 1-1h3.5c.6 0 1 .4 1 1 0 1.3.2 2.5.6 3.6.1.3 0 .7-.2 1z"/></svg>
        <span>555-318-6207</span>
      </li>
      <li>
        <svg viewBox="0 0 24 24" aria-hidden="true"><path d="M7 3h10v4H7zM4 8h16a2 2 0 0 1 2 2v6h-4v5H6v-5H2v-6a2 2 0 0 1 2-2zm4 8v3h8v-3z"/></svg>
        <span>555-318-6209</span>
      </li>
      <li>
        <svg viewBox="0 0 24 24" aria-hidden="true"><path d="M2 5h20v14H2zm2 2v.5l8 5 8-5V7zm0 2.8V17h16V9.8l-8 5z"/></svg>
        <span>mel@melsapothecary-example.com</span>
      </li>
      <li>
        <svg viewBox="0 0 24 24" aria-hidden="true"><path d="M12 2a10 10 0 1 0 0 20 10 10 0 0 0 0-20zm6.9 6h-3a15 15 0 0 0-1.3-3.9A8 8 0 0 1 18.9 8zM12 4c.8 1.1 1.5 2.5 1.9 4h-3.8c.4-1.5 1.1-2.9 1.9-4zM4.3 14a8 8 0 0 1 0-4h3.4a16 16 0 0 0 0 4zm.8 2h3a15 15 0 0 0 1.3 3.9A8 8 0 0 1 5.1 16zm3-8h-3a8 8 0 0 1 4.3-3.9C8.8 5.3 8.4 6.6 8.1 8zM12 20c-.8-1.1-1.5-2.5-1.9-4h3.8c-.4 1.5-1.1 2.9-1.9 4zm2.3-6H9.7a14 14 0 0 1 0-4h4.6a14 14 0 0 1 0 4zm.3 5.9c.6-1.2 1-2.5 1.3-3.9h3a8 8 0 0 1-4.3 3.9zm1.7-5.9a16 16 0 0 0 0-4h3.4a8 8 0 0 1 0 4z"/></svg>
        <span>www.melsapothecary-example.com</span>
      </li>
      <li>
        <svg viewBox="0 0 24 24" aria-hidden="true"><path d="M12 2a7 7 0 0 0-7 7c0 5.2 7 13 7 13s7-7.8 7-13a7 7 0 0 0-7-7zm0 9.5a2.5 2.5 0 1 1 0-5 2.5 2.5 0 0 1 0 5z"/></svg>
        <span>7134 North Brook Lane<br>Maple Ridge, ND 58214</span>
      </li>
    </ul>

    <div class="brand-lockup">
      <span class="dot" aria-hidden="true"></span>
      <span class="brand-name">Mel's Apothecary</span>
    </div>

    <p class="store-hours">
      <span class="label">Store hours:</span> Monday-Friday <span class="time">9 am- 6 pm</span>
      Saturday <span class="time">9 am- 1 pm</span>
      Sunday <span class="time">Closed</span>
    </p>

    <div class="base-band" aria-hidden="true"></div>
  </section>

  <section class="card back" aria-label="Card back, brand side">
    <div class="band band-top" aria-hidden="true"></div>
    <div class="brand-block">
      <div class="brand-lockup">
        <span class="dot" aria-hidden="true"></span>
        <span class="brand-name">Mel's Apothecary</span>
      </div>
      <p class="website">www.melsapothecary-example.com</p>
    </div>
    <div class="band band-bottom" aria-hidden="true"></div>
  </section>

</main>
</body>
</html>
```